New Business Card Design Project

I need a design for business cards, i am an electrical business called "Tandor Electrical and Communications" i need the cards to be double sided with the company logo on the back (attached) the front needs to say my company name, web site, email address, telephone number, and ABN number and electrical license number. I am open to different arrangements of the information but would like the background to be incorporating something electrical or something that looks smart. open to all additional ideas also.

The company colours are orange and grey see logo attached.

Business Name: Tandor Electrical and Communications
Website: tandorelectricalandcomms.example.au
Email: brent@tandorelectricalandcomms.example.au
Telephone(mobile): 0481203967
ABN: 71829034618
Lic No: 830472F

Target Market(s)

Business entities, Project Managers, Accounts, Clients

Industry/Entity Type

Electrician

Contact Information for Business Card

I need a design for business cards, i am an electrical business called "Tandor Electrical and Communications" i need the cards to be double sided with the company logo on the back (attached) the front needs to say my company name

Font styles to use
Serif
Sans Serif

Colors
f37122
5c5c5c

Requirements
Must have
• Must have the Logo on the back open to different ways of it being on the back but had in mind to keep it central but again open to other options
Nice to have
• A real modern cool background that is eye catching yet contemporary
Should not have
• No backgrounds of a light bulb or plug or anything like that

```html
<!DOCTYPE html>
<html lang="en">
<head>
<meta charset="utf-8">
<title>Tandor Electrical and Communications – Business Card</title>
<link rel="stylesheet" href="https://fonts.googleapis.com/css2?family=Saira:wght@400;500&family=Arimo:wght@400&display=swap">
<style>
  :root {
    --backdrop: #8f9090;
    --card-dark: #4a4a4d;
    --card-light: #ebebeb;
    --strip: #e4e4e4;
    --orange: #e8a021;
    --grey-text: #4f4f52;
    --light-text: #eeeeee;
    --rule: #8a8a8d;
  }
  * { margin: 0; padding: 0; box-sizing: border-box; }
  html, body { width: 1105px; height: 1200px; overflow: hidden; }
  body { background: var(--backdrop); position: relative; font-family: "Arimo", Arial, sans-serif; }

  .card { position: absolute; left: 102px; width: 900px; height: 513px; }
  .card-front { top: 62px; background: var(--card-dark); }
  .card-back { top: 628px; background: var(--card-light); }

  .brand { position: absolute; display: flex; align-items: center; gap: 18px; font-family: "Saira", sans-serif; font-weight: 500; }
  .brand-dot { flex: none; border-radius: 50%; background: var(--orange); }
  .brand-name { display: flex; flex-direction: column; line-height: 1; }
  .brand-word { letter-spacing: 0.06em; }
  .brand-tag { letter-spacing: 0.04em; margin-top: 8px; }

  .card-front .brand { right: 45px; top: 70px; color: var(--light-text); }
  .card-front .brand-dot { width: 34px; height: 34px; }
  .card-front .brand-word { font-size: 76px; }
  .card-front .brand-tag { font-size: 17px; }

  .holder { position: absolute; left: 42px; top: 242px; right: 40px; font-family: "Saira", sans-serif; }
  .holder-name { color: var(--orange); font-size: 33px; font-weight: 400; letter-spacing: 0.02em; line-height: 1; }
  .holder-role { display: flex; align-items: flex-end; gap: 2px; margin-top: 8px; color: var(--light-text); font-size: 22px; line-height: 1; }
  .holder-role::after { content: ""; flex: 1; height: 1px; background: var(--rule); margin-bottom: 2px; }

  .contacts { position: absolute; left: 42px; top: 335px; list-style: none; color: var(--light-text); }
  .contacts li { display: flex; align-items: center; gap: 14px; height: 36px; }
  .contacts svg { width: 22px; height: 22px; flex: none; }
  .contact-phone { font-size: 24px; }
  .contact-email, .contact-web { font-size: 20px; }

  .registration { position: absolute; right: 38px; top: 370px; text-align: right; color: var(--light-text); font-family: "Saira", sans-serif; font-size: 24px; line-height: 35px; }

  .card-strip { position: absolute; left: 0; right: 0; bottom: 0; height: 38px; background: var(--strip); border-top: 4px solid var(--orange); }

  .card-back .brand { left: 50%; top: 50%; transform: translate(-50%, -50%); color: var(--grey-text); gap: 26px; }
  .card-back .brand-dot { width: 52px; height: 52px; }
  .card-back .brand-word { font-size: 128px; }
  .card-back .brand-tag { font-size: 27px; margin-top: 10px; }
</style>
</head>
<body>
  <section class="card card-front" aria-label="Business card front">
    <div class="brand">
      <span class="brand-dot"></span>
      <div class="brand-name">
        <span class="brand-word">TANDOR</span>
        <span class="brand-tag">ELECTRICAL &amp; COMMUNICATIONS</span>
      </div>
    </div>

    <div class="holder">
      <p class="holder-name">BRENT HALLOWAY</p>
      <p class="holder-role">CEO/FOUNDER</p>
    </div>

    <ul class="contacts">
      <li class="contact-phone">
        <svg viewBox="0 0 22 22" aria-hidden="true"><rect x="5" y="1" width="12" height="20" rx="2" fill="none" stroke="var(--orange)" stroke-width="2.4"/><rect x="9" y="16" width="4" height="2" fill="var(--orange)"/></svg>
        <span>0481203967</span>
      </li>
      <li class="contact-email">
        <svg viewBox="0 0 22 22" aria-hidden="true"><rect x="2" y="5" width="18" height="12" fill="var(--orange)"/><path d="M2 5 L11 12 L20 5" fill="none" stroke="var(--card-dark)" stroke-width="1.6"/></svg>
        <span>brent@tandorelectricalandcomms.example.au</span>
      </li>
      <li class="contact-web">
        <svg viewBox="0 0 22 22" aria-hidden="true"><circle cx="11" cy="11" r="9" fill="var(--orange)"/><path d="M11 2 C6 7 6 15 11 20 M11 2 C16 7 16 15 11 20 M2 11 H20" fill="none" stroke="var(--card-dark)" stroke-width="1.3"/></svg>
        <span>tandorelectricalandcomms.example.au</span>
      </li>
    </ul>

    <div class="registration">
      <p>ABN: 71829034618</p>
      <p>Lic No: 830472F</p>
    </div>

    <div class="card-strip"></div>
  </section>

  <section class="card card-back" aria-label="Business card back">
    <div class="brand">
      <span class="brand-dot"></span>
      <div class="brand-name">
        <span class="brand-word">TANDOR</span>
        <span class="brand-tag">ELECTRICAL &amp; COMMUNICATIONS</span>
      </div>
    </div>
  </section>
</body>
</html>
```